Quarrel Ridge Advisory Business Card

Quarrel Ridge Advisory is a company that provides consulting services to the Mining Industry.

Whilst Quarrel Ridge Advisory is an Australian based company its client base is the global mining industry.

The essence of Quarrel Ridge Advisory is its a can do organisation that can make a difference to its clients by providing quality assistance and form lasting relationships.
Updates

Target Market(s)

The global Mining Industry.

Industry/Entity Type

Mining

Font styles to use
Serif

Colors

Designer to choose colors to be used in the design.

Requirements
Nice to have
• My thinking is the card would look good in black given the logo.

I would like to see written on the back side of the card " Providing Metallurgical, Management and Corporate Services to the Mining Industry"

```html
<!DOCTYPE html>
<html lang="en">
<head>
<meta charset="utf-8">
<title>Quarrel Ridge Advisory – Business Card</title>
<link rel="stylesheet" href="https://fonts.googleapis.com/css2?family=Lato:wght@400;700;900&display=swap">
<style>
  :root {
    --stage: #2b2b2b;
    --card: #1f1f1f;
    --card-back: #1c1c1c;
    --accent: #f5a31a;
    --ink-light: #f2f2f2;
    --ink-muted: #cfcfcf;
    --gloss: #0e0e0e;
    --gloss-text: #383838;
  }
  * { box-sizing: border-box; margin: 0; padding: 0; }
  html, body { width: 1200px; height: 800px; overflow: hidden; }
  body {
    background: var(--stage);
    font-family: "Lato", Arial, sans-serif;
    display: flex;
    align-items: center;
    justify-content: center;
    gap: 50px;
  }
  .card {
    width: 540px;
    height: 310px;
    border-radius: 16px;
    position: relative;
    box-shadow: 0 10px 30px rgba(0,0,0,.45);
  }

  /* Front */
  .card--front { background: var(--card); }
  .brand-mark {
    position: absolute;
    left: 36px;
    bottom: 40px;
    width: 190px;
    font-weight: 900;
    font-size: 27px;
    line-height: 1.05;
    text-transform: uppercase;
    color: var(--accent);
  }
  .details {
    position: absolute;
    left: 268px;
    top: 34px;
    right: 20px;
  }
  .holder-name {
    color: var(--accent);
    font-weight: 700;
    font-size: 19px;
  }
  .holder-role {
    color: var(--ink-light);
    font-size: 14px;
    margin-top: 2px;
  }
  .contact-list {
    list-style: none;
    margin-top: 26px;
  }
  .contact-list li {
    display: flex;
    align-items: center;
    gap: 8px;
    color: var(--ink-light);
    font-size: 11.5px;
    line-height: 1;
    margin-bottom: 7px;
    white-space: nowrap;
  }
  .contact-list svg { width: 12px; height: 12px; flex: none; }
  .office {
    margin-top: 22px;
    color: var(--ink-light);
    font-size: 12px;
    line-height: 1.45;
  }
  .office-name {
    color: var(--accent);
    font-weight: 700;
    font-size: 14px;
    margin-bottom: 2px;
  }

  /* Back */
  .card--back {
    background: var(--card-back);
    display: flex;
    flex-direction: column;
    align-items: center;
    justify-content: center;
    text-align: center;
    padding: 0 50px;
  }
  .brand-mark--gloss {
    font-weight: 900;
    font-size: 40px;
    line-height: 1.05;
    text-transform: uppercase;
    color: var(--gloss);
  }
  .tagline {
    margin-top: 26px;
    color: var(--gloss-text);
    font-weight: 700;
    font-size: 14px;
    line-height: 1.5;
  }
</style>
</head>
<body>

  <section class="card card--front" aria-label="Business card front">
    <div class="brand-mark">Quarrel Ridge Advisory</div>

    <div class="details">
      <p class="holder-name">Harlan Voss</p>
      <p class="holder-role">President</p>

      <ul class="contact-list">
        <li>
          <svg viewBox="0 0 12 12" aria-hidden="true"><path fill="#f2f2f2" d="M3 1l2 2.3-1.1 1.2a6 6 0 0 0 3.6 3.6L8.7 7 11 9l-1.3 1.7C5.8 10.4 1.6 6.2 1.3 2.3z"/></svg>
          0400 555 218
        </li>
        <li>
          <svg viewBox="0 0 12 12" aria-hidden="true"><rect x="3" y="1" width="6" height="3" fill="#f2f2f2"/><rect x="1" y="4.5" width="10" height="5" rx="1" fill="#f2f2f2"/><rect x="3" y="8" width="6" height="3" fill="#1f1f1f" stroke="#f2f2f2"/></svg>
          0400 555 219
        </li>
        <li>
          <svg viewBox="0 0 12 12" aria-hidden="true"><rect x="1" y="2.5" width="10" height="7" fill="#f2f2f2"/><path d="M1 2.5l5 4 5-4" fill="none" stroke="#1f1f1f" stroke-width="1"/></svg>
          harlan.v@quarrelridge.com.au
        </li>
        <li>
          <svg viewBox="0 0 12 12" aria-hidden="true"><circle cx="6" cy="6" r="5" fill="none" stroke="#f2f2f2" stroke-width="1.2"/><ellipse cx="6" cy="6" rx="2" ry="5" fill="none" stroke="#f2f2f2"/><path d="M1 6h10" stroke="#f2f2f2"/></svg>
          www.quarrelridgeadvisory.com.au
        </li>
      </ul>

      <div class="office">
        <p class="office-name">Quarrel Ridge Advisory</p>
        <p>Suite 118, Lvl 4, Kestrel Road,</p>
        <p>NSW 2150</p>
      </div>
    </div>
  </section>

  <section class="card card--back" aria-label="Business card back">
    <div class="brand-mark--gloss">Quarrel Ridge Advisory</div>
    <p class="tagline">“Providing Metallurgical, Management and Corporate<br>Services to the Mining Industry”</p>
  </section>

</body>
</html>
```